Make it POP! Label design for Australian Skin Care range

I want to see elegance, femininity, luxury, glamour.
Design needs to compliment existing logo in style and colours; turquoise and silver (see file). text required (see file)
There are 5 different products with different text - same design required.
Please see file attached for the containers the labels will be applied to.

Target Market(s)

women over 35

Industry/Entity Type

Skin Care Product

Font styles to use
Sans Serif

Colors
33b8a4

Requirements
Must have
• Design in Turquoise and silver
• Sans Serif fonts, compliment existing logo (see file)
• contain text exactly as written (see file)
Nice to have
• Feminine, flowing lines/ shapes
Should not have
• Black, nothing bold or masculine. Nothing that looks clinical or medical

```html
<!DOCTYPE html>
<html lang="en">
<head>
<meta charset="utf-8">
<title>Lumi's Grace – Native Hydrating Serum Label</title>
<link rel="stylesheet" href="https://fonts.googleapis.com/css2?family=Quicksand:wght@400;500;600&family=Raleway:wght@700;800&family=Roboto+Condensed:wght@400;700&display=swap">
<style>
:root{
  --teal:#1fb9b4;
  --teal-deep:#009ea0;
  --teal-soft:#8ccfcc;
  --teal-pale:#d3eeed;
  --silver:#b9b9b9;
  --ink:#111;
  --white:#fff;
}
*{margin:0;padding:0;box-sizing:border-box}
html,body{width:1200px;height:934px;overflow:hidden;background:var(--white)}
.label{position:relative;width:1200px;height:934px;overflow:hidden;background:var(--white);font-family:'Quicksand',sans-serif}
.wave-area{position:absolute;left:0;top:300px;width:1200px;height:380px;
  background:linear-gradient(180deg,rgba(255,255,255,0) 0%,var(--teal-pale) 12%,var(--teal-soft) 22%,var(--teal-deep) 34%,var(--teal) 66%,var(--teal-soft) 80%,var(--teal-pale) 90%,rgba(255,255,255,0) 100%)}
.divider{position:absolute;left:600px;top:0;width:1px;height:934px;background:var(--ink)}
.brand{position:absolute;text-align:center}
.brand-mark{border-radius:50%;background:var(--teal);box-shadow:0 0 0 4px #d6d6d6;margin:0 auto}
.brand-name{font-family:'Quicksand',sans-serif;font-weight:600;color:var(--silver);letter-spacing:.55em;white-space:nowrap}
.front-brand{left:0;width:600px;top:58px}
.front-brand .brand-mark{width:120px;height:120px}
.front-brand .brand-name{font-size:22px;margin-top:22px;padding-left:.55em}
.tagline{position:absolute;left:0;width:584px;top:240px;text-align:center;color:var(--teal);font-size:19px;line-height:23px;letter-spacing:.03em}
.product-title{position:absolute;left:0;width:594px;top:474px;text-align:center;font-family:'Raleway',sans-serif;font-weight:800;font-size:35px;line-height:48px;letter-spacing:.01em;
  background:linear-gradient(180deg,#ffffff 30%,#d2d2d2 65%,#f4f4f4);-webkit-background-clip:text;background-clip:text;color:transparent;filter:drop-shadow(1px 1px 1px rgba(0,0,0,.25))}
.key-ingredients{position:absolute;left:0;width:594px;top:708px;text-align:center;color:var(--teal);font-size:23px;line-height:33px}
.skin-pill{position:absolute;left:202px;top:782px;width:184px;height:35px;border-radius:18px;background:var(--teal);color:var(--white);font-size:21px;line-height:35px;text-align:center}
.footer-bar{position:absolute;left:0;top:868px;width:1200px;height:66px;border-top:5px solid #c9c9c9;background:linear-gradient(90deg,var(--teal),var(--teal-deep))}
.net-wt{position:absolute;left:64px;top:886px;color:var(--white);font-size:17px}
.net-wt strong{font-size:25px;font-weight:600}
.vegan-badge{position:absolute;left:448px;top:845px;width:110px;height:110px;border-radius:50%;background:var(--teal);border:5px solid #cfcfcf;text-align:center;font-family:'Roboto Condensed',sans-serif;font-weight:700;color:var(--white)}
.vegan-badge .pct{display:block;font-size:28px;line-height:28px;margin-top:18px}
.vegan-badge .word{display:block;font-size:22px;line-height:22px;margin-top:3px}
.back-brand{left:600px;width:596px;top:56px}
.back-brand .brand-mark{width:86px;height:86px}
.back-brand .brand-name{font-size:15px;margin-top:16px;padding-left:.55em}
.info-box{position:absolute;left:656px;top:208px;width:479px;height:376px;border:2px solid var(--teal);border-radius:12px;background:rgba(255,255,255,.85);padding:34px 30px 0 30px;
  font-family:'Roboto Condensed',sans-serif;font-size:17.8px;line-height:22.5px;color:var(--ink);text-align:justify}
.info-title{position:absolute;left:702px;top:188px;width:386px;height:40px;border-radius:20px;background:var(--teal);color:var(--white);font-family:'Raleway',sans-serif;font-weight:700;font-size:24px;line-height:40px;text-align:center}
.info-box p{margin-bottom:14px}
.info-box .lead{color:var(--teal);font-weight:700}
.batch{position:absolute;left:672px;top:680px;font-family:'Roboto Condensed',sans-serif;font-size:24px;line-height:38px;color:var(--ink)}
.origin{position:absolute;left:673px;top:832px;font-size:22px;color:var(--ink)}
.website{position:absolute;left:669px;top:882px;font-size:23px;letter-spacing:.06em;color:var(--white);font-weight:500}
</style>
</head>
<body>
<div class="label">
  <div class="wave-area" role="img" aria-label="Flowing turquoise wave decoration across the label"></div>

  <section class="front-panel">
    <div class="brand front-brand">
      <div class="brand-mark"></div>
      <div class="brand-name">LUMI'S GRACE</div>
    </div>
    <p class="tagline">Natural Nourishing<br>Australian Skin Care</p>
    <h1 class="product-title">NATIVE<br>HYDRATING SERUM</h1>
    <p class="key-ingredients">With<br>Quandong • Lilli Pilli • Kakadu Plum</p>
    <div class="skin-pill">All Skin Types</div>
  </section>

  <div class="footer-bar"></div>
  <div class="net-wt">Net Wt.: <strong>30ml</strong></div>
  <div class="vegan-badge"><span class="pct">100%</span><span class="word">VEGAN</span></div>

  <div class="divider"></div>

  <section class="back-panel">
    <div class="brand back-brand">
      <div class="brand-mark"></div>
      <div class="brand-name">LUMI'S GRACE</div>
    </div>
    <div class="info-box">
      <p><span class="lead">To Apply :</span> Apply a pearl sized amount between fingertips and warm before gently pressing and smoothing over face, neck and décolletage, avoiding eye area.</p>
      <p><span class="lead">Ingredients :</span> Aloe Barbadensis (Aloe Vera) Gel*, Aloe Barbadensis (Aloe Vera) Extract*, Citrus Glauca (Desert Lime)*, Santalum Acuminnatum (Quandong)*, Syzygium Leuhmannii (Lilli Pilli)*, Hibiscus Sabdariffa (Wild Rosella)*, Terminalia Ferninandiana (Kakadu Plum)*, Backhousia Citriodora (Lemon Myrtle) Oil, Lavandula Angustifolia (Australian Lavender) Oil, Citrus Aurantium Dulcis (Australian Orange) Oil - * Organic Ingredients</p>
      <p><span class="lead">Caution :</span> For external use only. Avoid contact with eyes. If irritation occurs, discontinue use.</p>
    </div>
    <h2 class="info-title">NATIVE HYDRATING SERUM</h2>
    <div class="batch">Batch No. :<br>Mfg. Date :<br>Expiry Date :</div>
    <p class="origin">Made in Australia</p>
    <p class="website">www.lumisgrace.com.au</p>
  </section>
</div>
</body>
</html>
```